Business Card Design Project for Electrical Company

We need a business card designed for a new Electrical Company called Dorvel Electrical Solutions, i dont mind if only Dorvel Electrical is used. We are a domestic and commercial Electrical Company that provides a range of Electrical Services. Our Company colours are Fluro Yellow and Black with the Lightning bolt picture attached.I have attached a card that has been made i think it is rather basic and am looking for something more. the font of Dorvel Electrical has been used on our car graphics as well as the lightning bolt. i want to keep them the same so we can brand our business. Some things we want on the front of the card are Dorvel Electrical Solutions, Owen Platt, 0438516274, admin@dorvelelectrical.example, Lic No 58342, Servicing CQ Region. But we want Owens name seperate to the phone number as its the phone number for the office, owen wont be answering the phone so we are thinking we dont want to give that impression. What do you think? with all that if you have complete different font designs please submit what you think would work best. keeping in mind our company name and details as well as coulors.

Industry/Entity Type

Business

```html
<!DOCTYPE html>
<html lang="en">
<head>
<meta charset="utf-8">
<title>Dorvel Electrical Solutions – Business Card Concepts</title>
<link rel="stylesheet" href="https://fonts.googleapis.com/css2?family=Oswald:wght@400;600;700&family=PT+Serif:ital,wght@0,400;0,700;1,400&display=swap">
<style>
  :root{
    --lime:#d4f01c;
    --ink:#000;
    --paper:#fff;
  }
  *{box-sizing:border-box;margin:0;padding:0}
  html,body{width:1200px;height:815px;overflow:hidden;background:var(--paper)}
  body{position:relative;font-family:"PT Serif",Georgia,serif;color:var(--ink)}

  .card{position:absolute;overflow:hidden;border:1px solid var(--ink);display:flex;flex-direction:column;align-items:center}
  .card--light{background:var(--paper)}
  .card--dark{background:var(--ink);color:var(--paper)}

  .stripe{position:absolute;top:-1px;bottom:-1px;width:12px;border-left:2px solid var(--ink);border-right:2px solid var(--ink);background:var(--lime)}
  .stripe--left{left:10px}
  .stripe--right{right:10px}

  .wordmark{font-family:"Oswald",Arial,sans-serif;font-weight:700;text-transform:uppercase;line-height:.92;color:var(--ink);letter-spacing:1px}
  .wordmark span{display:block}
  .wordmark--sm{font-size:38px}

  .name{font-family:"Oswald",Arial,sans-serif;font-weight:600;text-transform:uppercase;font-size:20px;letter-spacing:.5px}
  .role{font-style:italic;font-size:13px}
  .rule{height:2px;background:currentColor}
  .tagline{font-family:"Oswald",Arial,sans-serif;font-weight:700;font-size:24px}
  .contact{font-weight:700;font-size:14px;white-space:nowrap}
  .services{list-style:none;text-align:center;font-weight:700;font-size:14.5px;line-height:21px}
  .divider{display:flex;align-items:center;gap:6px}
  .divider i{display:block;width:14px;height:2px;background:currentColor}
  .divider b{display:block;width:6px;height:14px;background:currentColor}

  /* concept one */
  .c1-front{left:45px;top:22px;width:357px;height:257px;padding:22px 40px 0}
  .c1-front .wordmark{align-self:flex-start;margin-left:20px}
  .c1-back{left:45px;top:288px;width:357px;height:241px;padding:12px 30px 0}
  .c1-back .contact{font-size:12px;letter-spacing:-.2px}

  /* concept two */
  .c2-front{left:432px;top:30px;width:365px;height:234px}
  .c2-front .head{width:100%;background:var(--ink);color:var(--paper);text-align:center;padding:4px 0 4px}
  .c2-front .head .name{font-size:24px;line-height:1.1}
  .c2-front .lic{position:absolute;right:18px;top:58px;font-size:9px;font-weight:700}
  .c2-front .wordmark{font-size:40px;margin-top:22px;align-self:flex-start;margin-left:30px}
  .c2-front .foot{position:absolute;left:0;right:0;bottom:0;height:50px;background:var(--ink);padding:8px 10px}
  .c2-front .foot .boxed{border:2px solid var(--paper);color:var(--paper);text-align:center;font-family:"Oswald",Arial,sans-serif;font-weight:400;letter-spacing:1.5px;font-size:22px;line-height:30px;text-transform:uppercase}
  .c2-back{left:437px;top:291px;width:356px;height:234px;background:var(--ink);color:var(--paper);padding:0 8px}
  .c2-back .head{font-family:"Oswald",Arial,sans-serif;font-weight:600;font-size:17px;text-transform:uppercase;line-height:26px}
  .c2-back .box{background:var(--paper);color:var(--ink);width:100%;height:176px;padding-top:5px;display:flex;justify-content:center}
  .c2-back .services{font-size:14px;line-height:20.5px}
  .c2-back .contact{line-height:30px}

  /* concept three */
  .c3-front{left:831px;top:22px;width:364px;height:239px;background:var(--ink);color:var(--paper)}
  .c3-front .top{width:100%;height:128px;background:var(--paper);border-bottom:6px solid var(--lime);padding:14px 0 0 14px}
  .c3-front .top .wordmark{font-size:34px}
  .c3-back{left:827px;top:291px;width:365px;height:232px;padding-top:10px}
  .c3-back .services{font-size:14px;line-height:20px}
  .c3-back .boxed{border:2px solid var(--paper);font-family:"Oswald",Arial,sans-serif;font-weight:700;font-size:18px;padding:0 12px;line-height:26px;margin-top:6px}

  .alt-label{position:absolute;left:633px;top:680px;font-family:"Oswald",Arial,sans-serif;font-weight:700;font-size:19px;text-transform:uppercase}
  .alt-mark{position:absolute;left:890px;top:570px;width:240px;height:240px}
</style>
</head>
<body>

<section class="card card--light c1-front">
  <div class="stripe stripe--left"></div><div class="stripe stripe--right"></div>
  <div class="wordmark wordmark--sm"><span>Dorvel</span><span>Electrical</span><span style="font-size:26px">Solutions</span></div>
  <div class="rule" style="width:180px;margin-top:10px"></div>
  <div class="name" style="margin-top:4px">Owen Platt</div>
  <div class="role">Licensed Electrician</div>
  <div class="rule" style="width:180px;margin-top:3px"></div>
  <div class="tagline" style="margin-top:10px">Servicing CQ Region!</div>
</section>

<section class="card card--light c1-back">
  <div class="stripe stripe--left"></div><div class="stripe stripe--right"></div>
  <ul class="services">
    <li>Light &amp; Power</li><li>TV &amp; Data</li><li>Renovations</li><li>Test &amp; Tagging</li>
    <li>Residential</li><li>Design &amp; Installation</li><li>Air Conditioning Installation</li><li>Smoke Detectors</li>
  </ul>
  <div class="divider" style="margin-top:6px"><i></i><b></b><i></i></div>
  <div class="rule" style="width:180px;margin-top:6px"></div>
  <div class="contact" style="margin-top:4px">0438516274 &nbsp;admin@dorvelelectrical.example</div>
</section>

<section class="card card--light c2-front">
  <div class="head">
    <div class="name">Owen Platt:</div>
    <div class="role">Licensed Electrician</div>
  </div>
  <div class="lic">Lic no. 58342</div>
  <div class="wordmark"><span>Dorvel</span><span>Electrical</span><span style="font-size:28px">Solutions</span></div>
  <div class="foot"><div class="boxed">Servicing CQ Region!</div></div>
</section>

<section class="card c2-back">
  <div class="head">Having problems or need assistance with:</div>
  <div class="box">
    <ul class="services"><li>Light &amp; Power</li><li>TV &amp; Data</li><li>Renovations</li><li>Test &amp; Tagging</li>
    <li>Residential</li><li>Design &amp; Installation</li><li>Air Conditioning Installation</li><li>Smoke Detectors</li></ul>
  </div>
  <div class="contact">• 0438516274 • admin@dorvelelectrical.example •</div>
</section>

<section class="card c3-front">
  <div class="top">
    <div class="wordmark"><span>Dorvel</span><span>Electrical</span><span style="font-size:24px">Solutions</span></div>
  </div>
  <div class="rule" style="width:160px;margin-top:8px;height:1px"></div>
  <div class="name" style="font-size:18px">Owen Platt</div>
  <div class="rule" style="width:120px;height:1px"></div>
  <div class="role">Licensed Electrician</div>
  <div class="divider" style="margin-top:4px"><i></i><b></b><i></i></div>
  <div class="contact" style="margin-top:8px;font-size:13.5px">• 0438516274 • admin@dorvelelectrical.example •</div>
</section>

<section class="card card--dark c3-back">
  <ul class="services"><li>Light &amp; Power</li><li>TV &amp; Data</li><li>Renovations</li><li>Test &amp; Tagging</li>
  <li>Residential</li><li>Design &amp; Installation</li><li>Air Conditioning Installation</li><li>Smoke Detectors</li></ul>
  <div class="divider" style="margin-top:4px"><i></i><b></b><i></i></div>
  <div class="boxed">Servicing CQ Region!</div>
</section>

<div class="alt-label">Alternative logo? -----&gt;</div>
<svg class="alt-mark" viewBox="0 0 240 240" aria-label="Dorvel Electrical alternative mark">
  <circle cx="120" cy="120" r="108" fill="none" stroke="#000" stroke-width="12"/>
  <text x="120" y="114" text-anchor="middle" font-family="Oswald, Arial, sans-serif" font-weight="700" font-size="34">DORVEL</text>
  <text x="120" y="148" text-anchor="middle" font-family="Oswald, Arial, sans-serif" font-weight="700" font-size="34">ELECTRICAL</text>
</svg>

</body>
</html>
```